Business Card for Graphic Design Firm

This project is for a new graphic design firm based in New Jersey called Velmoth. We outsource graphic design and marketing jobs. We want to communicate that this is a professional company but it as well creative and artistic. This card may be used as a horizontal double sided paper card or a vertical single sided translucent card so feel free to submit designs in whichever format or both.
Updates

Reason: Extending the deadline because I'm not exactly satisfied with the designs so far.

Please view the updated project brief

Target Market(s)

Adults aged 25-60

Industry/Entity Type

Graphic Design

Font styles to use
Serif
Sans Serif

Requirements
Nice to have
• Maybe a triangular pattern around the edges similar to our logo

```html
<!DOCTYPE html>
<html lang="en">
<head>
<meta charset="utf-8">
<title>Velmoth Business Card</title>
<link href="https://fonts.googleapis.com/css2?family=Lato:wght@400;700&display=swap" rel="stylesheet">
<style>
  :root {
    --backdrop: #3b3c3d;
    --paper: #ffffff;
    --teal: #0b7a96;
    --teal-deep: #0f6e8a;
    --sky: #4ec3de;
    --orange: #f58a24;
    --slate: #5d6b70;
    --ink: #6a6a6a;
  }
  * { margin: 0; padding: 0; box-sizing: border-box; }
  html, body { width: 1200px; height: 1000px; overflow: hidden; }
  body {
    background: var(--backdrop);
    position: relative;
    font-family: "Lato", sans-serif;
    color: var(--ink);
  }
  .card {
    position: absolute;
    background: var(--paper);
    box-shadow: 0 3px 8px rgba(0,0,0,0.35);
    overflow: hidden;
  }
  .card-back { left: 180px; top: 149px; width: 568px; height: 332px; }
  .pattern-fill {
    position: absolute; inset: 0;
    background: linear-gradient(135deg, var(--teal) 0%, var(--sky) 40%, var(--orange) 75%, var(--slate) 100%);
  }
  .card-front { left: 446px; top: 528px; width: 569px; height: 332px; }
  .brand-block {
    position: absolute; left: 40px; top: 84px; width: 244px;
    display: flex; flex-direction: column; align-items: center;
  }
  .brand-mark {
    width: 44px; height: 44px; background: var(--teal); margin-bottom: 48px;
  }
  .brand-name {
    font-size: 32px; font-weight: 400; letter-spacing: 3px;
    color: #6d6d6d; text-transform: uppercase;
  }
  .details { position: absolute; left: 329px; top: 32px; }
  .person-name { font-size: 19px; font-weight: 700; color: var(--teal-deep); line-height: 24px; }
  .person-role { font-size: 15px; color: var(--ink); line-height: 20px; }
  .contact-list { list-style: none; margin-top: 22px; }
  .contact-list li {
    display: flex; align-items: center; gap: 7px;
    font-size: 13.5px; line-height: 22px; color: var(--ink);
  }
  .contact-list svg { width: 15px; height: 15px; flex: none; fill: var(--teal); }
  .company-name { margin-top: 26px; font-size: 15px; font-weight: 700; color: var(--teal-deep); line-height: 20px; }
  .company-address { font-size: 13.5px; line-height: 20px; color: var(--ink); }
  .footer-band { position: absolute; left: 0; bottom: 0; width: 100%; height: 20px; background: var(--teal); }
</style>
</head>
<body>
  <section class="card card-back">
    <div class="pattern-fill" role="img" aria-label="Repeating pattern of teal, sky blue, orange and slate triangles covering the card back"></div>
  </section>

  <section class="card card-front">
    <div class="brand-block">
      <div class="brand-mark"></div>
      <div class="brand-name">Velmoth</div>
    </div>

    <div class="details">
      <div class="person-name">Daniel Marsh</div>
      <div class="person-role">President</div>

      <ul class="contact-list">
        <li>
          <svg viewBox="0 0 16 16" aria-hidden="true"><path d="M4 1.5l2.2 3-1.3 1.4c.8 1.8 2.2 3.2 4 4l1.4-1.3 3 2.2-1.2 2.4C7 13 3 9 1.8 3.1z"/></svg>
          555 014 2290
        </li>
        <li>
          <svg viewBox="0 0 16 16" aria-hidden="true"><path d="M4 1h8v4H4zM1 6h14v6h-3v3H4v-3H1zM5 10v4h6v-4z"/></svg>
          555 014 2290
        </li>
        <li>
          <svg viewBox="0 0 16 16" aria-hidden="true"><path d="M1 3h14v10H1zM2.5 4.5L8 9l5.5-4.5v-.2h-11z"/></svg>
          daniel.m@velmoth.com
        </li>
        <li>
          <svg viewBox="0 0 16 16" aria-hidden="true"><circle cx="8" cy="8" r="6.5" fill="none" stroke="#0b7a96" stroke-width="1.6"/><path d="M5 4c2 1 1 3 3 3s1 3 3 4l-1 2c-2-1-3-3-5-3z"/></svg>
          www.velmoth.com
        </li>
      </ul>

      <div class="company-name">Velmoth</div>
      <div class="company-address">Suite 118, St. 9, Harbor Lane,<br>NJ 07030</div>
    </div>

    <div class="footer-band"></div>
  </section>
</body>
</html>
```